WP website design (Talbot)

We need a wordpress design for an established auction and real estate company based in Iowa. The winning design will incorporate a professional color scheme with company logo in a clean layout. The design needs to consider that this will be developed on a responsive theme. Colors are those that will highlight the logo.

Industry/Entity Type

Real Estate

Font styles to use
Sans Serif

Colors

Designer to choose colors to be used in the design.

Requirements
Must have
• navigation:
1)Home 2) Auction Calendar 3) Real Estate Listings 4) Services 5) About Us 6) Contact Us

Client mentions liking the http://www.pexworthsales.com site. Site will have no 'swooshes' as this will be developed on a responsive theme. Designs will needs to reflect this. Site will have slideshow - perhaps in the header of the site. Use stock real estate photo for initial image.

Home page will feature the text below and and auction list (as seen in pexworthsales.com). Widgets will include:
1) social icons (Chatterly, WorkNest and RSS )
2) testimonials widget
3) featured auctions widget
4) email signup form (name and email fields)

Footer will have the company logo, contact info, and affiliation logos (attached to project)

(homepage text)
Talbot Real Estate & Auction Company is located in West Central Iowa in the county seat town of Marlow County, Marlow Center, Iowa.

Dale R. Talbot, Auctioneer/Realtor, is the current owner and has been active as the main Auctioneer and Broker since 1982. Dale is the fourth generation of Auctioneers serving the area since 1901.

Since 1901 and four generations of Auctioneers, Talbot Real Estate & Auction Company has strived to offer honest and professional auction and real estate services.

We offer complete auction services, including Auctioneering, Clerking/Cashiering, and complete sale managment. Experienced in the auction sales of real estate, farms, farm machinery & equipment, estate and household sales, antique auctions, and business liquidations.

Our real estate agency handles the sales of residential, farm, recreational, and light commercial business properties and we have continued to be the #1 real estate firm in Marlow County for the past several years.

Member of the Continental Bidcallers Guild, Prairie Bidcallers League and the Allied Parishes Council of Brokers.

Please feel free to contact us for more information about your auction and/or real estate needs.

```html
<!DOCTYPE html>
<html lang="en">
<head>
<meta charset="utf-8">
<title>Talbot Real Estate &amp; Auction Co</title>
<link href="https://fonts.googleapis.com/css2?family=Open+Sans:ital,wght@0,400;0,600;0,700;1,400&family=Arimo:ital,wght@0,400;0,700;1,400&display=swap" rel="stylesheet">
<style>
:root{
  --green-bg:#1f5a2c;
  --green-dark:#1b4d27;
  --green-nav-top:#2f7a3f;
  --green-nav-bot:#1c5228;
  --green-btn:#22803f;
  --green-title:#1d5e2a;
  --panel:#333333;
  --panel-edge:#bdbdbd;
  --text:#333333;
  --heading:#3a3a3a;
  --footer:#262626;
  --footer-bar:#1a1a1a;
  --footer-text:#cfcfcf;
  --white:#ffffff;
}
*{margin:0;padding:0;box-sizing:border-box}
html,body{width:929px;height:1200px;overflow:hidden}
body{background:var(--green-bg);font-family:Arimo,Arial,sans-serif;color:var(--text);position:relative}
.page{position:absolute;left:78px;top:0;width:772px;height:1054px;background:var(--white)}
.abs{position:absolute}
.brand{left:12px;top:20px;font-family:"Open Sans",sans-serif;font-weight:700;font-size:40px;color:var(--green-dark);letter-spacing:1px}
.brand-sub{left:14px;top:70px;font-family:"Open Sans",sans-serif;font-weight:700;font-size:9px;color:var(--green-dark);letter-spacing:.5px}
.social{top:28px;display:flex;gap:12px;right:20px}
.social a{width:40px;height:40px;border-radius:5px;background:var(--green-title);color:#fff;font-family:"Open Sans",sans-serif;font-weight:600;font-size:8px;text-decoration:none;display:flex;align-items:center;justify-content:center}
.social a.rss{background:#f39a1c}
.nav{left:7px;top:103px;width:757px;height:41px;background:linear-gradient(var(--green-nav-top),var(--green-nav-bot));display:flex;align-items:center}
.nav a{color:#fff;text-decoration:none;font-family:"Open Sans",sans-serif;font-weight:600;font-size:11px;padding:0 14px;border-right:1px solid rgba(255,255,255,.2);line-height:20px}
.nav a:last-child{border:none}
.hero{left:8px;top:158px;width:548px;height:269px;background:linear-gradient(180deg,#c9d6e4 0%,#b7a76a 45%,#8d8550 70%,#4f7a35 100%)}
.signup-title{left:560px;top:158px;width:204px;height:43px;background:var(--green-dark);border:1px solid #0f3318;color:#fff;font-family:"Open Sans",sans-serif;font-weight:600;font-size:17px;display:flex;align-items:center;padding-left:12px;gap:10px}
.panel{background:var(--panel);border:1px solid var(--panel-edge);color:#fff}
.signup{left:560px;top:206px;width:204px;height:222px;padding:16px 18px;font-size:10.5px;line-height:17px}
.field{width:172px;height:27px;background:#fff;border-radius:4px;color:#666;font-size:10px;padding-left:12px;display:flex;align-items:center;margin-top:14px}
.field+.field{margin-top:23px}
.subscribe{margin-top:22px;width:96px;height:28px;border-radius:4px;background:var(--green-btn);font-family:"Open Sans",sans-serif;font-size:14px;display:flex;align-items:center;justify-content:center}
h2{font-family:"Open Sans",sans-serif;color:var(--heading)}
.welcome{left:13px;top:448px;font-size:18px;font-weight:600}
.intro{left:17px;top:483px;width:512px;font-size:9.6px;line-height:13.6px}
.intro p{margin-bottom:14px}
.intro p.strong{font-weight:700}
.upcoming{left:17px;top:778px;font-size:18px;font-weight:400}
.card{left:16px;top:819px;width:486px;height:168px;border:1px solid #d6d6d6;border-radius:5px;background:linear-gradient(#fbfbfb,#ececec)}
.card h3{position:absolute;left:13px;top:12px;font-size:12.5px;font-weight:700;color:var(--green-title)}
.card-photo{left:15px;top:39px;width:133px;height:82px;border:2px solid #ccc;background:linear-gradient(180deg,#b7d0e2,#7a9a7a 55%,#5b5f66)}
.live{left:157px;top:41px;font-size:10px;font-weight:700;color:var(--green-btn)}
.desc{left:157px;top:57px;width:300px;font-size:10px;line-height:13.6px}
.meta{left:157px;font-size:10px}
.meta b{margin-right:4px}
.tools{left:20px;top:133px;display:flex;align-items:center;font-size:10.5px}
.tools span{display:flex;align-items:center;gap:5px;padding-right:10px}
.tools .sep{border-left:1px solid #ccc;height:24px;margin-right:10px;padding:0}
.bid{left:157px;top:132px;width:198px;height:23px;background:var(--green-dark);border-radius:3px;color:#fff;font-size:9.6px;font-weight:700;display:flex;align-items:center;justify-content:center}
.pager{left:154px;top:1005px;display:flex;gap:13px;align-items:center;font-size:8px;color:#999}
.pager i{font-style:normal;width:16px;height:15px;background:#666;color:#fff;display:flex;align-items:center;justify-content:center}
.side-h{left:560px;font-size:18px;font-weight:400}
.featured{left:560px;top:486px;width:204px;height:259px;padding:0 17px;font-size:10px}
.feat-photo{left:17px;top:56px;width:177px;height:103px;border:2px solid #fff;background:linear-gradient(180deg,#c3d6e8,#8a6a4e 55%,#4b7a34)}
.testi{left:560px;top:792px;width:204px;height:210px;font-style:italic;font-size:10px;line-height:15.5px}
.quote{font-family:Georgia,serif;font-size:16px;font-style:normal;line-height:12px}
.testi-open{left:20px;top:20px}
.testi-text{left:21px;top:40px;width:172px}
.testi-close{left:174px;top:156px}
.testi-name{left:100px;top:178px;font-size:11.5px}
.footer{left:0;top:1054px;width:929px;height:112px;background:var(--footer)}
.contact{left:79px;top:20px;font-size:9.6px;line-height:14px;color:var(--footer-text)}
.badges{left:595px;top:40px;display:flex;gap:10px;align-items:center}
.badge{width:36px;height:36px;background:#cfcfcf}
.badge.round{border-radius:50%}
.foot-brand{left:738px;top:40px;font-family:"Open Sans",sans-serif;font-weight:700;font-size:28px;color:#cfcfcf}
.copy{left:0;top:1166px;width:929px;height:34px;background:var(--footer-bar);color:#fff;font-size:10.4px;display:flex;align-items:center;justify-content:center}
.copy u{margin:0 3px}
</style>
</head>
<body>
<div class="page">
  <div class="abs brand">TALBOT</div>
  <div class="abs brand-sub">REAL ESTATE AND AUCTION CO · SINCE 1901</div>
  <nav class="abs social">
    <a href="#">Chatterly</a><a href="#">WorkNest</a><a href="#" class="rss">RSS</a>
  </nav>
  <nav class="abs nav">
    <a href="#">HOME</a><a href="#">AUCTION CALENDAR</a><a href="#" style="padding:0 24px">REAL ESTATE LISTINGS</a><a href="#" style="padding:0 34px">SERVICES</a><a href="#" style="padding:0 24px">ABOUT US</a><a href="#">CONTACT US</a>
  </nav>
  <div class="abs hero" role="img" aria-label="Slideshow photo of a two-storey yellow family house with a landscaped front garden"></div>

  <div class="abs signup-title">
    <svg width="26" height="18" viewBox="0 0 26 18"><rect x="1" y="1" width="24" height="16" fill="none" stroke="#fff" stroke-width="2"/><path d="M1 1l12 9 12-9" fill="none" stroke="#fff" stroke-width="2"/></svg>
    EMAIL SIGN-UP
  </div>
  <div class="abs panel signup">
    Subscribe below to receive email alerts of upcoming auctions.
    <div class="field">Name</div>
    <div class="field">Email Address</div>
    <div class="subscribe">Subscribe</div>
  </div>

  <h2 class="abs welcome">Welcome to talbot real estate &amp; auticon</h2>
  <div class="abs intro">
    <p>Talbot Real Estate &amp; Auction Company is located in West Central Iowa in the county seat town of Marlow County, Marlow Center, Iowa.</p>
    <p>Dale R. Talbot, Auctioneer/Realtor, is the current owner and has been active as the main Auctioneer and Broker since 1982. Dale is the fourth generation of Auctioneers serving the area since 1901.</p>
    <p>Since 1901 and four generations of Auctioneers, Talbot Real Estate &amp; Auction Company has striv<br>ed to offer honest and professional auction and real estate services.</p>
    <p>We offer complete auction services, including Auctioneering, Clerking/Cashiering, and complete sale managment. Experienced in the auction sales of real estate, farms, farm machinery &amp; equipment, estate and household sales, antique auctions, and business liquidations.</p>
    <p>Our real estate agency handles the sales of residential, farm, recreational, and light commercial business properties and we have continued to be the #1 real estate firm in Marlow County for the past several years.</p>
    <p>Member of the Continental Bidcallers Guild, Prairie Bidcallers League and the Allied Parishes Council of Brokers.</p>
    <p class="strong">Please feel free to contact us for more information about your auction and/or real estate needs.</p>
  </div>

  <h2 class="abs upcoming">Upcoming Auctions</h2>
  <div class="abs card">
    <h3>ABSOLUTE ONLINE ONLY AUCTION – ANTIQUES &amp; COLLECTIBLES</h3>
    <div class="abs card-photo" role="img" aria-label="Photo of an auction crowd gathered in front of a house"></div>
    <div class="abs live">LIVE ON-SITE AUCTION</div>
    <div class="abs desc">Harrow BS3F High Lift, 600 Series Fenwick tractor w/Stanway Loader, Dune buggy, 1207 KR Cutditioner: SHOP &amp;</div>
    <div class="abs meta" style="top:95px"><b>Begins:</b> Saturday, March 16, 2013 at 10:00 AM EDT</div>
    <div class="abs meta" style="top:115px"><b>Location:</b> 2290 Millrace Road Fairview, KY 40099</div>
    <div class="abs tools">
      <span><svg width="11" height="11" viewBox="0 0 11 11"><circle cx="4.5" cy="4.5" r="3.3" fill="none" stroke="#222" stroke-width="1.6"/><path d="M7 7l3.3 3.3" stroke="#222" stroke-width="1.8"/></svg>Details</span>
      <span class="sep"></span>
      <span><svg width="13" height="10" viewBox="0 0 13 10"><rect x=".5" y=".5" width="12" height="9" fill="none" stroke="#222"/><path d="M2 8l3-4 2 2 2-2 2 4z" fill="#222"/></svg>Gallery</span>
    </div>
    <div class="abs bid">Click here for our online Bidding site</div>
  </div>
  <div class="abs pager">
    <span>&laquo; Previous</span><i>1</i><i>2</i><i>3</i><i>4</i><i>5</i><i>6</i><i>7</i><i>8</i><span>Next &raquo;</span>
  </div>

  <h2 class="abs side-h" style="top:453px">Featured Aution</h2>
  <div class="abs panel featured">
    <div style="margin-top:26px">Multi Estate &amp; Consignment Auction</div>
    <div class="abs feat-photo" role="img" aria-label="Photo of a brick two-storey house for the featured auction"></div>
    <div class="abs" style="left:22px;top:178px;width:170px;line-height:14px"><b>Start Date/ Time:</b> Saturday, April 13, 2013 At 10:00 Am</div>
    <div class="abs" style="left:19px;top:216px">Multi Estate &amp; Consignment Auction</div>
  </div>

  <h2 class="abs side-h" style="top:757px">Clients Testimonials</h2>
  <div class="abs panel testi">
    <div class="abs quote testi-open">&ldquo;</div>
    <p class="abs testi-text">Lorem Ipsum has been the indus-try's standard dummy text ever since the 1500s, when an unknown printer took a galley of type and sc rambled it to make a type speci men book.It has survived not only five centuries, but also the leap</p>
    <div class="abs quote testi-close">&rdquo;</div>
    <div class="abs testi-name">Ellen Marsh</div>
  </div>
</div>

<footer class="abs footer">
  <div class="abs contact">
    OFFICE : (620) 555-0144<br>FAX : (620) 555-0133<br>Email : office@talbotauction.net<br><br>Address: 118 W. Oak St., Harlan KS<br>Mailing Address: PO Box 208, Harlan, KS
  </div>
  <div class="abs badges">
    <div class="badge round"></div><div class="badge"></div><div class="badge"></div>
  </div>
  <div class="abs foot-brand">TALBOT</div>
</footer>
<div class="abs copy">Copyright © 2014 <u>Talbot Real Estate &amp; Auctions</u> All Rights Reserved.</div>
</body>
</html>
```